*** Einladungsdesign für Start-up Event gesucht ***
Zielgruppe
Für eine innovative Start-up Veranstaltung suchen wir ein stylishes, progressives Layout für die Einladungskarten. Die Veranstaltung heißt
#PlansOfTomorrow
und soll als schlichter Schriftzug in die Einladungen eingearbeitet sein. Die exakte Schriftart hierfür etc. wird noch übermittelt. Im Gegensatz das restliche Design gerne futuristisch und modern gehalten sein. Dennoch insgesamt hochwertiger Gesamteindruck
Aufgabenstellung
Name: #PlansOfTomorrow
Daten: 4 Seiten
Deckblatt.
linke Innenseite: kurzer Text/Grußwort:
YOUNG. CREATIVE. NIGHT.
Das Internet hat die Welt verändert und sich tief in unserer Gesellschaft verankert. Es ist die Chance unserer Generation diese Digitalisierung zu nutzen und die Welt von morgen weiterzuentwickeln
Freuen Sie sich auf eine inspirierende Nacht im Zeichen der „young leading minds of our time“. Ein Podium für Macher von heute und morgen.
FAST. FORWARD. FUTURE.
rechte Innenseite: Einladungstext
Wir freuen uns
_______________________________ (hier wird Name handschriftlich eingetragen)
zur exklusiven #PlansOfTomorrow-Night
einladen zu dürfen.
Datum: 01. Februar 2015
Uhrzeit: ab 20:30 Uhr
Ort: xxxxxx, Anfahrt über xxxxxxx
r.s.v.p. bis zum 14. Januar 2014 unter xxxxxxx
Rückseite: Sponsoren & Partner der Veranstaltung
Stehen noch nicht fest, daher bitte einfach mit ca. 5 farbigen Logos (z.B. Vemko AG) arbeiten.
Farbwelt: Gerne an verschiedenen Grautönen, Schwarz und Rot orientieren.
Format: Gängiges Format, 4C (Sonderfarben & Stanzformate können gerne vorgeschlagen werden),
Versand: Print (ca. 200 Stück) & Mail
Mögliche Motive: zB 3D-Formen, grobe Pixel, etc.
Nach Rücksprache kann der Designer auch in die Veranstaltung eingearbeitet werden oder sich vor Ort den Gründern und Wirtschaftsentscheidern präsentieren.

```html
<!DOCTYPE html>
<html lang="de">
<head>
<meta charset="utf-8">
<title>#PlansOfTomorrow – Einladung</title>
<link rel="stylesheet" href="https://fonts.googleapis.com/css2?family=Exo+2:wght@400;500&family=Share+Tech+Mono&display=swap">
<style>
  :root {
    --red: #e3412b;
    --red-soft: rgba(227, 65, 43, .55);
    --salmon-soft: rgba(239, 138, 108, .45);
    --grey: #9b9b9b;
    --grey-soft: rgba(155, 155, 155, .4);
    --ink: #3a3a3a;
    --paper: #ffffff;
    --bg: #ffffff;
    --display: "Exo 2", sans-serif;
    --mono: "Share Tech Mono", monospace;
  }
  * { box-sizing: border-box; margin: 0; padding: 0; }
  html, body { width: 1200px; height: 906px; overflow: hidden; background: var(--bg); }
  .canvas { position: relative; width: 1200px; height: 906px; }
  .spread {
    position: absolute; left: 93px; width: 986px; height: 360px;
    background: var(--paper); overflow: hidden;
    box-shadow: 0 2px 6px rgba(0,0,0,.12);
  }
  .spread--outside { top: 62px; }
  .spread--inside { top: 472px; }
  .fold { position: absolute; top: 0; left: 493px; width: 1px; height: 100%; background: rgba(0,0,0,.08); }
  .page { position: absolute; top: 0; width: 493px; height: 100%; }
  .page--left { left: 0; }
  .page--right { left: 493px; }

  /* Decorative artwork areas */
  .artwork { position: absolute; }
  .artwork--back-top { left: 0; top: 0; width: 493px; height: 185px;
    background: linear-gradient(170deg, var(--red-soft) 0%, var(--salmon-soft) 45%, rgba(255,255,255,0) 100%); }
  .artwork--back-bottom { left: 0; top: 290px; width: 493px; height: 70px;
    background: linear-gradient(to bottom, rgba(255,255,255,0) 0%, var(--grey-soft) 100%); }
  .artwork--cover-side { left: 700px; top: 0; width: 286px; height: 360px;
    background: linear-gradient(to right, rgba(255,255,255,0) 0%, var(--salmon-soft) 45%, var(--red-soft) 100%); }
  .artwork--cover-top { left: 493px; top: 0; width: 207px; height: 60px;
    background: linear-gradient(to bottom, var(--grey-soft) 0%, rgba(255,255,255,0) 100%); }
  .artwork--inner-top { left: 0; top: 0; width: 493px; height: 150px;
    background: linear-gradient(170deg, var(--grey-soft) 0%, var(--salmon-soft) 40%, rgba(255,255,255,0) 100%); }
  .artwork--inner-bottom { left: 0; top: 305px; width: 493px; height: 55px;
    background: linear-gradient(to bottom, rgba(255,255,255,0) 0%, var(--grey-soft) 100%); }
  .artwork--invite-top { left: 493px; top: 0; width: 493px; height: 80px;
    background: linear-gradient(to bottom, var(--red-soft) 0%, rgba(255,255,255,0) 100%); }
  .artwork--invite-side { left: 820px; top: 80px; width: 166px; height: 280px;
    background: linear-gradient(to right, rgba(255,255,255,0) 0%, var(--salmon-soft) 50%, var(--grey-soft) 100%); }

  /* Cover */
  .event-title {
    position: absolute; left: 34px; top: 122px;
    font-family: var(--display); font-weight: 500; font-size: 36px; line-height: 1.1;
    color: var(--ink); letter-spacing: 1px; text-transform: uppercase;
  }
  .event-title .hash { font-size: 28px; margin-right: 6px; }
  .event-title .accent { color: var(--red); }
  .event-title .line { display: block; }

  /* Sponsors */
  .sponsors {
    position: absolute; left: 36px; top: 214px; width: 440px;
    display: flex; justify-content: space-between; align-items: center;
  }
  .sponsor {
    display: flex; align-items: center; gap: 6px;
    font-family: var(--display); font-weight: 500; font-size: 16px; color: var(--ink);
  }
  .sponsor .mark { width: 14px; height: 14px; background: var(--red); }
  .sponsor .mark--round { border-radius: 50%; background: var(--grey); }
  .sponsors-caption {
    position: absolute; left: 0; top: 274px; width: 493px; text-align: center;
    font-family: var(--display); font-size: 11px; letter-spacing: 1.4px;
    color: var(--grey); text-transform: uppercase;
  }

  /* Inside left */
  .slogan {
    position: absolute; right: 35px;
    font-family: var(--display); font-weight: 500; font-size: 18px; line-height: 1.08;
    color: var(--ink); letter-spacing: 1px; text-transform: uppercase;
  }
  .slogan .accent { color: var(--red); }
  .slogan--top { top: 66px; text-align: left; }
  .slogan--bottom { top: 242px; text-align: right; }
  .greeting {
    position: absolute; left: 28px; top: 154px; width: 445px;
    font-family: var(--mono); font-size: 10.5px; line-height: 1.75; color: var(--ink);
  }

  /* Inside right */
  .invitation {
    position: absolute; left: 57px; top: 0;
    font-family: var(--mono); font-size: 11px; line-height: 1.4; color: var(--ink);
  }
  .invitation p { position: absolute; left: 0; white-space: nowrap; }
  .invitation .accent { color: var(--red); }
  .invitation .rsvp { font-size: 8px; letter-spacing: 1px; }
</style>
</head>
<body>
<main class="canvas">

  <section class="spread spread--outside" aria-label="Außenseite: Rückseite und Deckblatt">
    <div class="artwork artwork--back-top" role="img" aria-label="Abstrakte transparente Diagonalflächen in Rot, Lachs und Grau"></div>
    <div class="artwork artwork--back-bottom" role="img" aria-label="Abstrakte graue Diagonalflächen am unteren Rand"></div>
    <div class="artwork artwork--cover-top" role="img" aria-label="Abstrakte graue Flächen am oberen Rand"></div>
    <div class="artwork artwork--cover-side" role="img" aria-label="Abstrakte transparente Diagonalflächen in Rot, Lachs und Grau"></div>
    <div class="fold"></div>

    <div class="page page--left">
      <div class="sponsors">
        <span class="sponsor"><span class="mark mark--round"></span>Vemko AG</span>
        <span class="sponsor"><span class="mark"></span>Kassenwerk</span>
        <span class="sponsor">Vallora</span>
        <span class="sponsor"><span class="mark"></span>Stadtsparhaus</span>
      </div>
      <p class="sponsors-caption">Sponsoren &amp; Partner der Veranstaltung</p>
    </div>

    <div class="page page--right">
      <h1 class="event-title">
        <span class="line"><span class="hash">#</span>Plans</span>
        <span class="line accent">Of</span>
        <span class="line">Tomorrow</span>
      </h1>
    </div>
  </section>

  <section class="spread spread--inside" aria-label="Innenseiten: Grußwort und Einladung">
    <div class="artwork artwork--inner-top" role="img" aria-label="Abstrakte transparente Diagonalflächen in Grau und Lachs"></div>
    <div class="artwork artwork--inner-bottom" role="img" aria-label="Abstrakte graue Flächen am unteren Rand"></div>
    <div class="artwork artwork--invite-top" role="img" aria-label="Abstrakte rote Diagonalfläche am oberen Rand"></div>
    <div class="artwork artwork--invite-side" role="img" aria-label="Abstrakte transparente Diagonalflächen in Lachs und Grau"></div>
    <div class="fold"></div>

    <div class="page page--left">
      <p class="slogan slogan--top">Young.<br><span class="accent">Creative.</span><br>Night.</p>
      <p class="greeting">Das Internet hat die Welt verändert und sich tief in unserer Gesellschaft verankert. Es ist die Chance unserer Generation diese Digitalisierung zu nutzen und die Welt von morgen weiterzuentwickeln. Freuen Sie sich auf eine inspirierende Nacht im Zeichen der „young leading minds of our time“. Ein Podium für Macher von heute und morgen.</p>
      <p class="slogan slogan--bottom">Fast.<br>Forward.<br><span class="accent">Future.</span></p>
    </div>

    <div class="page page--right">
      <div class="invitation">
        <p style="top:100px">Wir freuen uns</p>
        <p style="top:148px">zur exklusiven #Plans<span class="accent">Of</span>Tomorrow-Night<br>einladen zu dürfen.</p>
        <p style="top:188px">Datum:&nbsp;&nbsp;&nbsp; <span class="accent">01.Februar 2015</span><br>Uhrzeit: ab 20:30 Uhr</p>
        <p style="top:226px">Ort: xxxxxx | Anfahrt über xxxxxxx</p>
        <p class="rsvp" style="top:250px">r.s.v.p. bis zum 14. Januar 2014 unter xxxxxxx</p>
      </div>
    </div>
  </section>

</main>
</body>
</html>
```